Men's enhance supplement package design (square form)

WHAT WE WANT TO TELL BY DESIGN:Male enhancement, enhance Sexual vitality, strong man, get (back) desire forsex, masculinity, booster.This supplement is not like Korvane but want to tell like Korvane by design.

Target Market(s)

Men who over 30 years old and feel lack of sexual desire.

```html
<!DOCTYPE html>
<html lang="en">
<head>
<meta charset="utf-8">
<title>L-Titanovir Original Formula – Dietary Supplement for Men</title>
<link rel="stylesheet" href="https://fonts.googleapis.com/css2?family=Montserrat:wght@300;400;500;600;700;800&display=swap">
<style>
  :root {
    --bg-light: #2e2e30;
    --bg-dark: #0b0b0c;
    --red: #e61c2e;
    --red-deep: #8e0d18;
    --silver-hi: #ffffff;
    --silver-mid: #c9cacc;
    --silver-low: #6e7074;
    --text-white: #ffffff;
    --text-grey: #cfcfd1;
    --text-soft: #bdbdc0;
    --tag-dark: #121214;
    --tag-mid: #2b2b2e;
  }
  html, body {
    margin: 0;
    padding: 0;
    width: 821px;
    height: 1200px;
    overflow: hidden;
    background: var(--bg-dark);
  }
  .package {
    display: block;
    width: 821px;
    height: 1200px;
  }
  .eyebrow {
    font-family: "Montserrat", sans-serif;
    font-weight: 300;
    font-size: 37px;
    fill: var(--text-grey);
    letter-spacing: 0.5px;
  }
  .product-name {
    font-family: "Montserrat", sans-serif;
    font-weight: 800;
    font-size: 96px;
    fill: var(--text-white);
  }
  .formula {
    font-family: "Montserrat", sans-serif;
    font-weight: 500;
    font-size: 44px;
    fill: var(--text-white);
  }
  .ingredient {
    font-family: "Montserrat", sans-serif;
    font-weight: 700;
    font-size: 29px;
    fill: var(--text-white);
  }
  .ingredient-light {
    font-weight: 400;
  }
  .supplement-label {
    font-family: "Montserrat", sans-serif;
    font-weight: 700;
    font-size: 29px;
    fill: var(--text-grey);
  }
  .count {
    font-family: "Montserrat", sans-serif;
    font-weight: 800;
    font-size: 98px;
    fill: var(--text-soft);
    letter-spacing: -4px;
  }
  .for-men {
    font-family: "Montserrat", sans-serif;
    font-weight: 700;
    font-size: 29px;
    fill: var(--text-white);
  }
  .tablets {
    font-family: "Montserrat", sans-serif;
    font-weight: 300;
    font-size: 27px;
    fill: var(--text-grey);
  }
</style>
</head>
<body>
<svg class="package" viewBox="0 0 1020 1490" preserveAspectRatio="none" xmlns="http://www.w3.org/2000/svg">
  <defs>
    <linearGradient id="bg-gradient" x1="0" y1="0" x2="1" y2="0.3">
      <stop offset="0" stop-color="var(--bg-light)"/>
      <stop offset="0.55" stop-color="#1b1b1d"/>
      <stop offset="1" stop-color="var(--bg-dark)"/>
    </linearGradient>
    <linearGradient id="red-gradient" x1="0" y1="0" x2="0.6" y2="1">
      <stop offset="0" stop-color="var(--red-deep)"/>
      <stop offset="0.45" stop-color="var(--red)"/>
      <stop offset="1" stop-color="#c4121f"/>
    </linearGradient>
    <linearGradient id="silver-gradient" x1="0" y1="0" x2="1" y2="1">
      <stop offset="0" stop-color="var(--silver-hi)"/>
      <stop offset="0.35" stop-color="var(--silver-mid)"/>
      <stop offset="0.7" stop-color="var(--silver-low)"/>
      <stop offset="1" stop-color="#d8d9db"/>
    </linearGradient>
    <linearGradient id="tag-gradient" x1="0" y1="0" x2="1" y2="0">
      <stop offset="0" stop-color="var(--tag-dark)"/>
      <stop offset="1" stop-color="var(--tag-mid)"/>
    </linearGradient>
    <linearGradient id="figure-gradient" x1="0" y1="0" x2="0.8" y2="1">
      <stop offset="0" stop-color="#b3121f"/>
      <stop offset="0.5" stop-color="#3a0b10"/>
      <stop offset="1" stop-color="#0a0a0a"/>
    </linearGradient>
  </defs>

  <!-- background -->
  <rect class="backdrop" x="0" y="0" width="1020" height="1490" fill="url(#bg-gradient)"/>

  <!-- red corner field and silver blade -->
  <polygon class="red-field" points="0,528 522,1490 0,1490" fill="url(#red-gradient)"/>
  <polygon class="silver-blade" points="0,475 376,622 214,660 648,1490 522,1490 0,528" fill="url(#silver-gradient)"/>

  <!-- header -->
  <text class="eyebrow" x="84" y="131">HIGH QUALITY</text>
  <text class="product-name" x="84" y="224" textLength="792" lengthAdjust="spacingAndGlyphs">L-TITANOVIR</text>
  <polygon class="formula-accent" points="105,248 140,248 172,315 137,315" fill="var(--red)"/>
  <text class="formula" x="133" y="297">Original Formula</text>

  <!-- hero figure area -->
  <rect class="hero-figure" role="img" aria-label="Illustration of a caped Spartan warrior running forward in red, black and white"
        x="430" y="345" width="515" height="895" rx="60" fill="url(#figure-gradient)"/>

  <!-- ingredient tags -->
  <g class="ingredient-tags">
    <polygon points="60,1237 405,1237 432,1287 87,1287" fill="url(#tag-gradient)"/>
    <text class="ingredient" x="95" y="1273">KRA CHAI DAHM</text>
    <polygon points="95,1300 440,1300 467,1350 122,1350" fill="url(#tag-gradient)"/>
    <text class="ingredient" x="130" y="1336">TONGKAT ALI</text>
    <polygon points="130,1362 470,1362 497,1412 157,1412" fill="url(#tag-gradient)"/>
    <text class="ingredient" x="160" y="1399">BCAA <tspan class="ingredient-light">and more</tspan></text>
  </g>

  <!-- pack details -->
  <g class="pack-details">
    <text class="supplement-label" x="627" y="1345">DIETARY SUPPLEMENT</text>
    <text class="count" x="663" y="1430">90</text>
    <polygon points="800,1364 955,1364 970,1402 800,1402" fill="var(--red)"/>
    <text class="for-men" x="806" y="1394">FOR MEN</text>
    <text class="tablets" x="806" y="1430">TABLETS</text>
  </g>
</svg>
</body>
</html>
```